Very Simple Web Redesign Project - Using Photoshop

Required is a very simple website home page redesign for the following site: http://www.kestrelslateworks.com.au/
I require this as a Photoshop design.
The basic look and feel of the site needs to remain.
Specifically the colours don't need to be changed.
The positioning of the site is currently correct for the target market.
The site does not need to be made super slick looking. Just upgraded to a new version.
The current text can all be used.
The only menus necessary are a horizontal menu at the top, and a simple horizontal text menu at the bottom of the page. Do NOT retain the vertical menu on the home page (having the items "Our Gallery", "Our Services", "Enquire Now").
Give the horizontal menu the following items:
Home | Slate Roof Repairs | Slate Reroofing | Slate Roof Benefits | Other Services | Photo Gallery | FAQ's | Free Quote | Contact Us
The picture of the house at the top RHS of the page needs to be reduced in size by approx 50% and moved to the top LHS of the page.
Please place the following text into the top of the page:
"Call Now: 0427 618 302"
Keep the four pictures on the home page layout. Some larger images attached.
Thanks,
Ned
Updates
Hi,
Thanks for all the designs.
I am working with my client to get which one they like the most.
Thanks,
Ned

```html
<!DOCTYPE html>
<html lang="en">
<head>
<meta charset="utf-8">
<title>Kestrel Slateworks</title>
<link href="https://fonts.googleapis.com/css2?family=Arimo:wght@400;700&display=swap" rel="stylesheet">
<style>
:root{
  --green-dark:#244d12;
  --green-nav:#2a5614;
  --green-mid:#3f8321;
  --green-glow:#93ba2e;
  --lime:#a6c513;
  --text:#111;
  --list-text:#d3e6c4;
  --white:#fff;
}
*{margin:0;padding:0;box-sizing:border-box}
html,body{width:1200px;height:1156px;overflow:hidden}
body{position:relative;background:var(--white);font-family:"Arimo",Arial,sans-serif;color:var(--text)}
.abs{position:absolute}
.topbar{left:0;top:0;width:1200px;height:30px;background:var(--green-dark)}
.toplinks{right:110px;top:7px;font-size:14px;color:var(--white)}
.toplinks span{margin:0 9px}
.header{left:0;top:30px;width:1200px;height:120px;background:radial-gradient(ellipse 260px 150px at 330px 30px,var(--green-glow),var(--green-mid) 100%)}
.brand-mark{left:140px;top:62px;width:56px;height:56px;background:var(--green-dark)}
.brand-name{left:232px;top:62px;font-size:40px;font-weight:700;color:var(--white);line-height:48px}
.nav{left:0;top:150px;width:1200px;height:60px;background:var(--green-nav)}
.nav ul{list-style:none;display:flex;justify-content:space-between;margin:0 110px;height:60px;align-items:center;font-size:16px;color:#eef5e6}
.headline{left:112px;top:264px;font-size:33px;font-weight:700;color:var(--green-dark);line-height:40px}
.headline .line2{display:block;margin-top:8px}
.headline .a{font-size:33px}
.headline .free{font-size:42px;color:var(--lime)}
.intro{left:111px;top:374px;width:390px;font-size:14px;line-height:20px;color:var(--green-nav)}
.phone{left:111px;top:479px;width:336px;height:62px;border-radius:31px;background:var(--green-dark);display:flex;align-items:center;padding-left:36px;gap:20px;color:var(--lime);font-size:35px;font-weight:700}
.photo{background:linear-gradient(160deg,#8a8f99,#5d6270)}
.p1{left:536px;top:277px;width:128px;height:128px}
.p2{left:536px;top:415px;width:128px;height:128px}
.p3{left:674px;top:275px;width:155px;height:268px;background:linear-gradient(180deg,#9fb2c4,#7d7f8c 45%,#d8c9a2 70%,#5f9a2c)}
.p4{left:834px;top:275px;width:250px;height:268px;background:linear-gradient(180deg,#b8c9dc,#6d7382 40%,#c9c9c4 75%,#7c8070)}
h2{position:absolute;top:602px;font-size:23px;font-weight:400;color:var(--text);line-height:30px}
.h-why{left:112px}
.h-spec{left:531px}
.why-text{left:111px;top:670px;width:392px;font-size:12px;line-height:20px}
.reasons{left:111px;top:736px;width:390px;list-style:none}
.reasons li{height:48px;margin-bottom:2px;background:radial-gradient(ellipse 220px 60px at 40% 50%,#3e7f22,#245012);color:var(--list-text);font-size:12px;display:flex;align-items:center;padding-left:18px}
.reasons li::before{content:"";width:6px;height:6px;border-radius:50%;background:var(--white);margin-right:12px}
.spec-text{left:531px;top:670px;width:565px;font-size:12px;line-height:20px}
.spec-text p{margin-bottom:40px}
.footer{left:0;top:1096px;width:1200px;height:60px;background:var(--green-dark);color:#d7e6cc;font-size:11px;letter-spacing:1px}
.footer .links{position:absolute;left:110px;top:23px}
.footer .links span{margin:0 11px}
.footer .copy{position:absolute;right:57px;top:23px;font-weight:700;color:#e4eedb}
</style>
</head>
<body>
<div class="abs topbar"></div>
<div class="abs toplinks">Free Quote<span>|</span>Contact Us</div>

<header class="abs header"></header>
<div class="abs brand-mark"></div>
<div class="abs brand-name">Kestrel Slateworks</div>

<nav class="abs nav">
  <ul>
    <li>Home</li><li>|</li><li>Slate Roof Repairs</li><li>|</li><li>Slate Reroofing</li><li>|</li><li>Slate Roof Benefits</li><li>|</li><li>Other Services</li><li>|</li><li>Photo Gallery</li>
  </ul>
</nav>

<div class="abs headline">Call now and arrange<span class="line2"><span class="a">a </span><span class="free">free quote</span></span></div>
<p class="abs intro">We service all inner city suburbs of Sydney roughly covering an area encompassing Gordon to Epping, Mosman to Bondi, Coogee to Kogarah and Kingsgrove to Burwood and Concord</p>
<div class="abs phone">
  <svg width="36" height="28" viewBox="0 0 36 28" aria-hidden="true"><path d="M2 9 Q18 -2 34 9 L31 14 L25 11 L25 7 Q18 5 11 7 L11 11 L5 14 Z" fill="#a6c513"/><path d="M9 13 L27 13 L32 27 L4 27 Z" fill="#a6c513"/><circle cx="18" cy="20" r="3.5" fill="#244d12"/></svg>
  <span>0427 618 302</span>
</div>

<div class="abs photo p1" role="img" aria-label="Photo of a window set in a slate roof"></div>
<div class="abs photo p2" role="img" aria-label="Photo of a dormer window on a slate roof"></div>
<div class="abs photo p3" role="img" aria-label="Photo of a conical slate turret roof"></div>
<div class="abs photo p4" role="img" aria-label="Photo of a restored slate roof on a period home"></div>

<h2 class="h-why">Why choose Kestrel Slateworks?</h2>
<h2 class="h-spec">Kestrel Slateworks - the Slate Roof Specialists</h2>

<p class="abs why-text">At Kestrel Slateworks we provide a variety of services in the upkeep, maintenance and or replacement of your slate and wood shingle roof.</p>
<ul class="abs reasons">
  <li>Lorem ipsum dolor sit amet, consectetur adipisicing</li>
  <li>Lorem ipsum dolor sit amet, consectetur adipisicing elit</li>
  <li>Lorem ipsum dolor sit amet, consectetur</li>
  <li>Lorem ipsum dolor sit amet, consectetur adipisicing</li>
  <li>Lorem ipsum dolor sit amet, consectetur adipisicing elit</li>
  <li>Lorem ipsum dolor sit amet, consectetur</li>
</ul>

<div class="abs spec-text">
  <p>At Kestrel Slateworks we specialize in the upkeep, maintenance, repair and replacement of all types of slate roof as well as wood shingles. We can track down the leak that just won't go away or give your house a complete re-roof. We can also provide all your guttering needs.</p>
  <p>Kestrel Slateworks is a small company and as such we do not have the overheads that larger companies do. Quality work and attention to detail are our trademark.</p>
  <p>All photos on this website consist of work which I have personally done. The above photos provide at a quick glance a reasonable cross section of the type of work I do.</p>
  <p>By clicking on the Photo Gallery link you can see other work including some before and after shots.</p>
  <p>Feel free to call at your earliest convenience to organise an obligation free quote or fill out a form by clicking on the Contact Us link below.</p>
</div>

<footer class="abs footer">
  <div class="links">Home<span>|</span>Legal Disclaimer<span>|</span>Terms of Use<span>|</span>Privacy Policy<span>|</span>FAQ<span>|</span>Sitemap</div>
  <div class="copy">© 2011 Kestrel Slateworks.</div>
</footer>
</body>
</html>
```